Website design for luxury private hair salon

I'm looking for someone to use my Logo and build me a website for my webpage www.lunetresses.com.au (You can have a look at it as it has every detail I need included on it already), however I want a fresh new appearance and it to look and feel super stylish.

I am thinking colours in black, with silver or white, beautiful hair images like the ones you'll see on the current webpage - the price list as per what you already see.

I will include a copy of my biz card on here, so you can see the feel of the card, and design a website with a similar feel. It is matt black with a foil silver.

Modern, but classic and fresh. I will also need you to be able to publish it to my URL for me as I have no idea how to do this. I need it up and running pronto!

The website will need to be able to be read clearly on all devices incluing smart phones and ipads. The URL is currently registered and hosted by Nimbo Vault

Thinking a Home Page - large logo etc and write up on who and what we offer
Services/Price List page - as per the price list on my current webpage
Contact Page - with a built in contact form.

Target Market(s)

Middle aged, fashionable, stylish women and men who enjoy luxury hair care and styling in an upmarket location.

Industry/Entity Type

Hair And Beauty

Number of Pages Required

3 page

Font styles to use
Other font styles liked:
• see my images for my current logo

Colors
000000
b2b2b2
a54499

Requirements
Must have
• Style
• Fast turnaround
• Be viewable on all devices, PC, ipads, smart phones
• Designer able to upload it so its a running website for me to my URL
Nice to have
• Just a really feminine, stylish website which is easy to read and shows some beautiful images of perfect hair
Should not have
• Browns, reds or orange colours.

```html
<!DOCTYPE html>
<html lang="en">
<head>
<meta charset="utf-8">
<title>Lune Tresses hair &amp; body — Home</title>
<link href="https://fonts.googleapis.com/css2?family=Great+Vibes&family=Lato:ital,wght@0,300;0,400;1,400&display=swap" rel="stylesheet">
<style>
  :root {
    --black: #000000;
    --sidebar-top: #1c1c1c;
    --sidebar-bottom: #080808;
    --silver: #b2b2b2;
    --silver-light: #d6d6d6;
    --nav-text: #c9c9c9;
    --divider: #2a2a2a;
    --edge: #4a4a4a;
    --panel-bg: rgba(20, 20, 20, 0.55);
    --panel-border: rgba(150, 150, 150, 0.45);
    --plum: #4a1463;
    --white: #ffffff;
    --social: #0a0a0a;
  }
  * { box-sizing: border-box; margin: 0; padding: 0; }
  html, body { width: 1200px; height: 540px; overflow: hidden; background: var(--black); }
  body { font-family: "Lato", sans-serif; }

  .site {
    position: relative;
    width: 1200px;
    height: 540px;
    display: flex;
  }

  .sidebar {
    width: 362px;
    height: 540px;
    background: linear-gradient(180deg, var(--sidebar-top) 0%, var(--sidebar-bottom) 100%);
    border-right: 1px solid var(--edge);
    position: relative;
  }

  .brand {
    position: absolute;
    top: 46px;
    left: 0;
    width: 362px;
    text-align: center;
    color: var(--silver-light);
    font-weight: 300;
  }
  .brand-name { display: block; font-size: 50px; letter-spacing: 1px; line-height: 1.1; }
  .brand-tagline { display: block; font-size: 25px; letter-spacing: 2px; margin-top: 8px; }

  .main-nav {
    position: absolute;
    top: 217px;
    left: 100px;
    width: 165px;
    list-style: none;
  }
  .main-nav li {
    height: 47px;
    line-height: 47px;
    text-align: center;
    border-bottom: 1px solid var(--divider);
  }
  .main-nav a {
    color: var(--nav-text);
    text-decoration: none;
    font-style: italic;
    font-size: 16px;
    letter-spacing: 0.2px;
  }

  .social-links {
    position: absolute;
    top: 452px;
    left: 0;
    width: 362px;
    display: flex;
    justify-content: center;
    gap: 22px;
  }
  .social-links span {
    width: 32px;
    height: 32px;
    border-radius: 50%;
    background: var(--social);
    display: block;
  }

  .hero {
    position: relative;
    flex: 1;
    height: 540px;
    overflow: hidden;
  }
  .hero-photo {
    position: absolute;
    inset: 0;
    background:
      radial-gradient(ellipse 200px 260px at 530px 170px, rgba(238, 220, 180, 0.85) 0%, rgba(210, 185, 140, 0.5) 45%, rgba(0,0,0,0) 100%),
      radial-gradient(ellipse 240px 300px at 580px 460px, rgba(18, 22, 34, 0.95) 0%, rgba(0,0,0,0) 100%),
      linear-gradient(120deg, #1a1712 0%, #0e0d0b 45%, #1e1a14 100%);
  }

  .welcome-panel {
    position: absolute;
    left: 150px;
    top: 225px;
    width: 556px;
    height: 247px;
    background: var(--panel-bg);
    border: 1px solid var(--panel-border);
    border-radius: 4px;
    text-align: center;
  }
  .welcome-title {
    font-family: "Great Vibes", cursive;
    font-weight: 400;
    color: var(--silver-light);
    font-size: 96px;
    line-height: 1;
    margin-top: 18px;
  }
  .welcome-sub {
    font-style: italic;
    color: var(--silver-light);
    font-size: 26px;
    margin-top: 2px;
  }
  .book-button {
    display: inline-block;
    margin-top: 12px;
    background: var(--plum);
    color: var(--white);
    font-size: 22px;
    font-weight: 400;
    text-decoration: none;
    width: 166px;
    height: 56px;
    line-height: 56px;
    border-radius: 3px;
  }
</style>
</head>
<body>
  <div class="site">
    <aside class="sidebar">
      <div class="brand">
        <span class="brand-name">Lune Tresses</span>
        <span class="brand-tagline">hair &amp; body</span>
      </div>
      <ul class="main-nav">
        <li><a href="#">HOME</a></li>
        <li><a href="#">SERVICES</a></li>
        <li><a href="#">PRICE LIST</a></li>
        <li><a href="#">CONTACT US</a></li>
      </ul>
      <div class="social-links" aria-label="Social media links">
        <span></span><span></span><span></span>
      </div>
    </aside>

    <main class="hero">
      <div class="hero-photo" role="img" aria-label="Photograph of a woman with long wavy platinum blonde hair and a dark wrap, against a softly blurred dark background"></div>
      <section class="welcome-panel">
        <h1 class="welcome-title">Welcome</h1>
        <p class="welcome-sub">to Lune Tresses hair &amp; body</p>
        <a class="book-button" href="#">BOOK NOW</a>
      </section>
    </main>
  </div>
</body>
</html>
```